Brightline Climate Vehicle Wrap for our new HVAC business. Wanting to have the best wrap on the road

We are looking to get our vehicles wrapped. We want something that is catchy and stands out. We have a logo already and would like to implement it into the wrap as well. We want a WOW factor when people see our vehicles coming down the road
It needs to say Heating & Cooling 330-617-AIRS (2477) on the it
When U want Cozy, U want Brightline Climate Systems

Target Market(s)

Residential & Light Commercial

Industry/Entity Type

Residential Heating & Cooling

Colors
0054AA
0677BA
7BADD7
CADEEF
E8F1F8
0094D4
00A9DD
6FCCEA
C7EBF8
E9F6FB
F0912C
F2A743
F7CA91
FBE8D2
FDF5EE
EE7325
F08F49
F5BC92
FAE3D3
FDF4ED

Requirements
Must have
• Eye catching graphics
Nice to have
• I would like to incorporate our logo into the wrap
Should not have
• We are open to anything

```html
<!DOCTYPE html>
<html lang="en">
<head>
<meta charset="utf-8">
<title>Brightline Climate Vehicle Wrap</title>
<link rel="stylesheet" href="https://fonts.googleapis.com/css2?family=Anton&family=Montserrat:ital,wght@0,800;1,800&display=swap">
<style>
  :root {
    --navy: #0054AA;
    --blue: #0677BA;
    --sky: #00A9DD;
    --sky-light: #6FCCEA;
    --sky-pale: #C7EBF8;
    --orange: #EE7325;
    --orange-deep: #D9621A;
    --amber: #F0912C;
    --white: #FFFFFF;
    --stage: #F4F6F8;
    --panel-edge: #DDE3E8;
  }
  html, body {
    margin: 0;
    padding: 0;
    width: 1200px;
    height: 720px;
    overflow: hidden;
    background: var(--stage);
  }
  .wrap-canvas {
    position: relative;
    width: 1200px;
    height: 720px;
  }
  .wrap-side {
    position: absolute;
    left: 50px;
    top: 100px;
    width: 1100px;
    height: 520px;
  }
  .panel { fill: var(--white); stroke: var(--panel-edge); stroke-width: 2; }
  .band-main { fill: var(--orange); }
  .shard-orange { fill: var(--orange); }
  .shard-amber { fill: var(--amber); }
  .shard-blue { fill: var(--sky); }
  .shard-navy { fill: var(--blue); }
  .slogan-band { fill: var(--sky); }
  .slogan-edge { fill: var(--blue); }
  .headline {
    font-family: "Montserrat", sans-serif;
    font-weight: 800;
    font-style: italic;
    font-size: 46px;
    fill: var(--white);
    letter-spacing: 2px;
  }
  .phone {
    font-family: "Anton", sans-serif;
    font-size: 52px;
    fill: var(--navy);
  }
  .slogan {
    font-family: "Anton", sans-serif;
    font-size: 18px;
    fill: var(--white);
    letter-spacing: 0.5px;
  }
  .brand-name {
    font-family: "Montserrat", sans-serif;
    font-weight: 800;
    font-size: 26px;
    fill: var(--orange);
  }
  .brand-dot { fill: var(--sky); }
</style>
</head>
<body>
<div class="wrap-canvas">
  <svg class="wrap-side" viewBox="0 0 1100 520" xmlns="http://www.w3.org/2000/svg">
    <defs>
      <linearGradient id="photoTone" x1="0" y1="0" x2="1" y2="1">
        <stop offset="0" stop-color="#C7EBF8"/>
        <stop offset="0.55" stop-color="#7BADD7"/>
        <stop offset="1" stop-color="#0677BA"/>
      </linearGradient>
      <clipPath id="panelClip">
        <rect x="0" y="0" width="1100" height="520" rx="28"/>
      </clipPath>
    </defs>

    <rect class="panel" x="0" y="0" width="1100" height="520" rx="28"/>

    <g clip-path="url(#panelClip)">
      <!-- right-side graphic shards -->
      <polygon class="shard-orange" points="840,30 1100,0 1100,520 800,520 930,330 800,350 900,130"/>
      <polygon class="shard-blue" points="900,18 1010,10 950,90"/>
      <polygon class="shard-navy" points="1030,60 1100,40 1100,180"/>
      <polygon class="shard-amber" points="1050,260 1100,240 1100,340"/>

      <!-- photo area -->
      <rect x="905" y="60" width="175" height="400" rx="14" fill="url(#photoTone)"
            role="img" aria-label="Photo of a woman adjusting a thermostat at home"/>
      <polygon class="shard-blue" points="1060,120 1100,90 1100,260 1070,300" opacity="0.85"/>
    </g>

    <!-- brand block -->
    <circle class="brand-dot" cx="380" cy="120" r="16"/>
    <text class="brand-name" x="406" y="129">Brightline Climate</text>

    <!-- headline band -->
    <polygon class="band-main" points="100,255 880,200 1000,180 860,260 80,315"/>
    <text class="headline" x="140" y="295" transform="rotate(-4 140 295)">HEATING &amp; COOLING</text>

    <!-- phone -->
    <text class="phone" x="150" y="395" transform="rotate(-4 150 395)">330-617-2477</text>

    <!-- slogan band -->
    <polygon class="slogan-edge" points="555,470 575,430 880,408 870,448"/>
    <polygon class="slogan-band" points="590,385 905,363 885,440 570,462"/>
    <text class="slogan" x="625" y="410" transform="rotate(-4 625 410)">WHEN U WANT COZY</text>
    <text class="slogan" x="598" y="442" transform="rotate(-4 598 442)">U WANT BRIGHTLINE CLIMATE SYSTEMS</text>
  </svg>
</div>
</body>
</html>
```